Postcard Design for Silver Lanterns

This will be a promotional postcard, 4 x 6 inches, to be sent, to let fans know about my next book. The cover art should be in color on one side; the copy for the back should be on half of the space (so there is room for an address. I've attached suggested copy. If I've given you too many words, please contact me.
Thank you -- Mira
Updates

I love both designs so far! One comment: Even if the type is small, I'd like a return address on the cards so I can keep my mailing list up-to-date. The address is P.O. Box 318, Dunmore, Maine 04672 Thank you!

Industry/Entity Type

Promotional

```html
<!DOCTYPE html>
<html lang="en">
<head>
<meta charset="utf-8">
<title>Silver Lanterns — Postcard</title>
<link rel="stylesheet" href="https://fonts.googleapis.com/css2?family=Tinos:ital,wght@0,400;0,700;1,400;1,700&family=Parisienne&family=Cinzel:wght@400&display=swap">
<style>
  :root {
    --ink-purple: #4a2b8e;
    --band-purple: #4b2d8f;
    --deep-purple: #2b1060;
    --paper: #ffffff;
    --script-pink: #e3187f;
    --scene-dark: #2a2230;
    --scene-gold: #b58b2a;
    --scene-violet: #5b4a9a;
    --cover-peach: #f3c9a0;
    --cover-green: #7fae4a;
    --text-dark: #1a1a1a;
  }
  * { margin: 0; padding: 0; box-sizing: border-box; }
  html, body { width: 1200px; height: 816px; overflow: hidden; background: var(--paper); }
  .postcard { position: relative; width: 1200px; height: 816px; overflow: hidden; background: var(--paper); }

  .scene-art {
    position: absolute; left: 0; top: 0; width: 1200px; height: 360px;
    background:
      radial-gradient(ellipse at 25% 20%, var(--scene-gold) 0%, transparent 45%),
      radial-gradient(ellipse at 85% 30%, #c9a86a 0%, transparent 40%),
      radial-gradient(ellipse at 10% 70%, var(--scene-violet) 0%, transparent 45%),
      linear-gradient(180deg, #6e5a2a 0%, var(--scene-dark) 100%);
  }
  .edges { position: absolute; left: 0; top: 0; width: 1200px; height: 816px; }

  .series-banner {
    position: absolute; left: 0; top: 88px; width: 620px; height: 90px;
    display: flex; align-items: center; padding-left: 104px;
    font-family: "Tinos", serif; font-style: italic; font-size: 31px; color: var(--paper);
    z-index: 2;
  }
  .series-banner strong { font-weight: 700; }

  .title {
    position: absolute; left: 114px; top: 384px;
    font-family: "Tinos", serif; font-weight: 400; font-size: 104px; line-height: 94px;
    color: var(--ink-purple); letter-spacing: 1px;
  }
  .series-name {
    position: absolute; left: 100px; top: 582px;
    font-family: "Parisienne", cursive; font-size: 42px; color: var(--script-pink);
  }

  .cover {
    position: absolute; left: 793px; top: 88px; width: 320px; height: 524px;
    overflow: hidden;
    box-shadow: 2px 3px 6px rgba(0,0,0,0.35);
    background:
      linear-gradient(180deg, var(--cover-peach) 0%, #e9b98a 45%, #8c6fa8 62%, var(--cover-green) 85%, #5e8a35 100%);
    font-family: "Tinos", serif; color: var(--ink-purple);
  }
  .cover-kicker, .cover-title {
    position: absolute; left: 0; width: 100%; text-align: center; white-space: nowrap;
  }
  .cover-kicker { top: 12px; font-family: "Parisienne", cursive; font-size: 15px; color: #6b1a5a; }
  .cover-title { top: 44px; font-family: "Cinzel", serif; font-size: 44px; line-height: 48px; color: var(--ink-purple); }
  .cover-tagline { position: absolute; top: 156px; right: 18px; font-style: italic; font-size: 13px; color: var(--text-dark); }
  .cover-author { position: absolute; top: 428px; left: 20px; font-family: "Cinzel", serif; font-size: 32px; color: var(--paper); white-space: nowrap; }
  .cover-note { position: absolute; top: 472px; left: 28px; font-size: 10px; font-style: italic; color: #ffe34d; }

  .website {
    position: absolute; left: 770px; top: 644px; width: 370px; text-align: center;
    font-family: "Tinos", serif; font-size: 25px; letter-spacing: 4px; color: var(--text-dark);
  }
  .website b { font-weight: 700; }
</style>
</head>
<body>
<main class="postcard">
  <div class="scene-art" role="img" aria-label="Painted parlor scene with a long-haired cat on a sofa, a purple armchair and a lamp"></div>

  <svg class="edges" viewBox="0 0 1200 816" aria-hidden="true">
    <polygon fill="#ffffff" points="0,312 40,304 90,314 150,300 210,310 270,298 330,308 400,296 470,306 540,294 610,304 680,296 760,306 840,298 920,310 1000,300 1080,312 1150,302 1200,310 1200,700 0,700"/>
    <polygon fill="#2b1060" points="0,664 60,672 130,660 200,670 280,658 360,668 440,656 520,666 600,654 680,664 760,676 840,662 920,672 1000,660 1080,670 1150,662 1200,668 1200,816 0,816"/>
    <polygon fill="#4b2d8f" points="0,88 575,88 620,178 0,178"/>
  </svg>

  <div class="series-banner">1st in new&nbsp;<strong>MIRA HOLLIS</strong>&nbsp;series!</div>

  <h1 class="title">SILVER<br>LANTERNS</h1>
  <p class="series-name">Harborside Lantern Mystery Series</p>

  <div class="cover" role="img" aria-label="Book cover painting of a cozy sitting room with a cat, cushions and a tea table">
    <span class="cover-kicker">A Harborside Lantern Mystery</span>
    <span class="cover-title">SILVER<br>LANTERNS</span>
    <span class="cover-tagline">Lit on arrival...</span>
    <span class="cover-author">Mira Hollis</span>
    <span class="cover-note">•First in a New Series!•</span>
  </div>

  <p class="website">www.<b>Mirahollis</b>.com</p>
</main>
</body>
</html>
```